Serene Spiritual Website Wanted for World Wide Organisation

We need a serene, clean web design for our organisation that works around the world.

What We Do
We aim to bring life into synergy across the world. We inspire, motivate, synchronise, and harmonise. We work with energy which is essential to all of life (environmental, human & animal). Our website must depict the spiritual element of being innately natural and reflect animism.

We have included a PDF attachment with details of the structure, navigation, and some websites for ideas/reference. The logo is also attached.
Updates

Target Market(s)

Anyone over 18yrs looking for answers to life's big questions or looking to develop themselves

Industry/Entity Type

Spiritual/wellbeing/Self Development

Number of Pages Required

5+ page

Requirements
Must have
• It must be serene and natural looking, it must incorporate the logo.
Nice to have
• We have included a Powerpoint document which may help you understand what we need, it is just an idea for structure and style, it is not set in stone so feel free to be as creative as you like!
Should not have
• Not clinical.

```html
<!DOCTYPE html>
<html lang="en">
<head>
<meta charset="utf-8">
<title>Luma Grove — Discover Your Spiritual Heart</title>
<link rel="stylesheet" href="https://fonts.googleapis.com/css2?family=Mulish:ital,wght@0,300;0,400;0,500;0,600;0,700;1,300;1,400&display=swap">
<style>
:root{
  --navy:#3f3f6c;
  --navy-deep:#37375f;
  --violet:#7b79b8;
  --lilac:#a9a8d4;
  --gold:#c8b35e;
  --cream:#fdfbf0;
  --mist:#f4f4f7;
  --ink:#3c3c5c;
  --text:#6e6e86;
  --white:#ffffff;
}
*{box-sizing:border-box;margin:0;padding:0}
html,body{width:1200px;height:5000px;overflow:hidden;background:var(--white)}
body{position:relative;font-family:"Mulish",sans-serif;color:var(--text)}
.abs{position:absolute}
p{font-size:12px;line-height:1.6}
.sprig{position:absolute;width:44px;height:34px;border-radius:50% 50% 45% 45%;background:radial-gradient(circle at 50% 60%,#d6c57a,#e8dca6 70%,transparent 72%)}
.section-title{position:absolute;font-weight:500;color:var(--ink);font-size:35px;text-align:center;width:1200px;left:0}
.section-lede{position:absolute;width:1200px;left:0;text-align:center}

/* hero */
.hero{left:78px;top:0;width:1042px;height:468px;background:linear-gradient(180deg,#ddd18a 0%,#cfc795 35%,#b3b1cc 75%,#a6a5d2 100%)}
.brand{position:absolute;top:42px;display:flex;align-items:center;gap:8px;font-weight:700;font-size:13px;letter-spacing:1.5px;color:var(--gold);text-transform:lowercase}
.brand .dot{width:22px;height:22px;border-radius:50%;background:var(--violet)}
.nav{position:absolute;top:40px;display:flex;gap:20px;font-size:11px;color:#6a6880}
.hero-title{position:absolute;top:144px;width:720px;font-size:61px;line-height:1.13;font-weight:600;color:var(--navy)}
.hero-frame{left:566px;top:316px;width:452px;height:330px;background:var(--white)}
.hero-photo{left:588px;top:342px;width:408px;height:302px;background:linear-gradient(160deg,#d9d2c8,#a99d91 55%,#5d5650)}

/* collage */
.frame{position:absolute;background:var(--white);box-shadow:0 4px 16px rgba(60,60,90,.18)}
.photo{position:absolute;left:8px;top:8px;right:8px;bottom:8px}
.quote{position:absolute;color:#fff;font-weight:300}

/* events */
.event-card{left:217px;top:1827px;width:280px;height:410px;background:var(--navy);box-shadow:0 8px 20px rgba(40,40,80,.25);overflow:hidden}
.tag{position:absolute;left:20px;top:26px;background:var(--lilac);color:var(--navy);font-size:9px;padding:3px 6px;letter-spacing:.5px}
.upcoming-head{left:627px;top:1825px;font-size:24px;font-weight:400;color:var(--navy);letter-spacing:.5px}
.event-row{position:absolute;left:610px;width:410px}
.date{position:absolute;left:0;width:90px;text-align:center}
.date b{display:block;font-size:28px;font-weight:400;color:var(--navy)}
.date i{display:block;width:40px;height:1px;background:var(--lilac);margin:4px auto}
.date span{font-size:10px;color:var(--text);letter-spacing:.5px}
.event-body{position:absolute;left:100px;width:280px}
.event-body h4{font-size:18px;font-weight:500;color:var(--navy);margin-bottom:8px}
.event-body p{font-size:10.5px;line-height:1.45}
.meta{display:flex;align-items:center;gap:6px;font-size:10px;margin-top:6px;color:var(--text)}
.link{display:inline-block;margin-top:12px;font-size:10.5px;color:var(--navy);text-decoration:underline}

/* about */
.about{left:78px;top:2353px;width:1042px;height:1123px;background:linear-gradient(180deg,var(--cream) 0%,#fbf8ea 70%,#ece8dc 100%)}
.person h3{font-size:23px;font-weight:400;color:var(--navy);margin-bottom:14px}
.person p{font-size:12.5px;line-height:1.65;margin-bottom:16px}
.person .spec{font-style:italic;color:#9a9aae}

/* what we do */
.service{position:absolute;top:3715px;width:408px;height:278px;overflow:hidden;box-shadow:0 6px 18px rgba(40,40,80,.2);color:#fff}
.service h3{position:absolute;left:48px;top:50px;font-size:21px;font-weight:400}
.service p{position:absolute;left:48px;top:92px;width:315px;font-size:12.5px;color:#e6e6f3}
.btn{position:absolute;left:48px;top:188px;padding:10px 28px;font-size:11.5px;font-weight:600;color:#fff;border-radius:4px}

/* wisdom */
.wisdom{left:78px;top:4099px;width:1042px;height:530px;background:var(--mist)}
.post{position:absolute;top:4342px;width:198px}
.post .thumb{height:136px}
.post h5{font-size:13px;font-weight:500;color:var(--ink);margin-top:26px;line-height:1.4}
.post small{display:block;font-size:8.5px;color:#9a9aae;margin-top:6px}
.post a{display:block;font-size:9.5px;color:var(--navy);text-decoration:underline;margin-top:22px}

/* footer */
.footer{left:78px;top:4718px;width:1042px;height:282px;background:var(--navy-deep);color:#d7d7ea}
.footer h6{font-size:11px;font-weight:600;color:#fff;margin-bottom:8px}
.footer h6::after{content:"";display:block;width:34px;height:1px;background:var(--gold);margin-top:6px}
.footer li{list-style:none;font-size:9.5px;line-height:27px}
.social{display:flex;gap:14px;margin-top:8px}
.social span{width:22px;height:22px;border-radius:50%;background:#fff}
</style>
</head>
<body>

<!-- Hero -->
<section class="abs hero" aria-label="Hero">
  <div class="brand" style="left:102px"><span class="dot"></span>luma grove</div>
  <nav class="nav" style="right:102px"><span>Events</span><span>About</span><span>Synergise</span><span>Wisdom</span><span>Shop</span></nav>
  <h1 class="hero-title" style="left:102px">Discover Your Spiritual Heart and Discover Peace</h1>
</section>
<div class="abs hero-frame"></div>
<div class="abs hero-photo" role="img" aria-label="Woman in a yoga prayer pose by the sea rocks"></div>

<!-- Welcome -->
<span class="sprig" style="left:578px;top:756px" role="img" aria-label="Gold leaf accent"></span>
<h2 class="section-title" style="top:794px">Welcome to Luma Grove</h2>
<p class="section-lede" style="top:850px;font-size:12.5px">Lorem ipsum dolor sit amet, consectetur adipiscing<br>elit, sed do eiusmod tempor incididunt ut labore et<br>dolore magna aliqua.</p>

<div class="frame" style="left:159px;top:962px;width:516px;height:436px">
  <div class="photo" role="img" aria-label="Woman meditating facing misty green mountains" style="background:linear-gradient(170deg,#c9d3dc,#9fb0b8 40%,#5f7a55 75%,#3d4e36)"></div>
  <div class="quote" style="left:152px;top:80px;width:340px;font-size:24px;line-height:1.3">“Yesterday I was clever, so I wanted to change the world. Today I am wise, so I am changing myself”.<br><i>— Elias Varn</i></div>
</div>
<div class="frame" style="left:700px;top:1074px;width:338px;height:214px">
  <div class="photo" role="img" aria-label="Stacked zen stones with a white flower on dark ground" style="background:linear-gradient(135deg,#2c2c2e,#1d1e20 60%,#3a3a38)"></div>
  <div class="quote" style="left:30px;top:30px;width:260px;font-size:12.5px;line-height:1.6;color:#f0e2a8">“For things to reveal themselves to us, we need to be ready to abandon our views about them.”<br><br><i>— Oren Sailo</i></div>
</div>
<div class="frame" style="left:272px;top:1314px;width:450px;height:236px">
  <div class="photo" role="img" aria-label="Stone seated buddha statue in front of a rock wall" style="background:linear-gradient(120deg,#6b4e3e,#8f6d55 50%,#5a3f31)"></div>
  <div class="quote" style="left:36px;top:64px;width:260px;font-size:22px;line-height:1.35">“ The purpose of our lives is to be happy.”<br><i>— Tenzin Arvo</i></div>
</div>
<div class="frame" style="left:750px;top:1322px;width:290px;height:182px">
  <div class="photo" role="img" aria-label="Dark wooden boards with a seashell" style="background:linear-gradient(135deg,#1f3340,#233d4a 60%,#2f4f58)"></div>
  <div class="quote" style="left:50px;top:48px;width:200px;font-size:12px;line-height:1.45">“Awakening is not changing who you are, but discarding who you are not.”<br>— Mira Kestel</div>
</div>

<!-- Events -->
<span class="sprig" style="left:594px;top:1656px" role="img" aria-label="Gold leaf accent"></span>
<h2 class="section-title" style="top:1694px;left:18px">Events</h2>
<p class="section-lede" style="top:1750px;left:18px;font-size:11px;line-height:1.5">Lorem ipsum dolor sit amet, consectetur adipiscing elit, sed do<br>eiusmod tempor incididunt ut labore et dolore magna aliqua.</p>

<article class="abs event-card">
  <span class="tag">CURRENT</span>
  <div class="abs" style="left:22px;top:58px;font-size:30px;color:#fff">23</div>
  <div class="abs" style="left:22px;top:100px;width:44px;height:1px;background:var(--lilac)"></div>
  <div class="abs" style="left:20px;top:108px;font-size:10px;color:#c6c6e0;letter-spacing:.5px">AUGUST</div>
  <h3 class="abs" style="left:22px;top:148px;width:245px;font-size:18px;font-weight:600;line-height:1.4;color:var(--gold)">The Cultivation Of One’s Own Intuitive Wisdom</h3>
  <p class="abs" style="left:22px;top:210px;width:220px;font-size:10px;line-height:1.45;color:#bdbdd8">Lorem ipsum dolor sit amet, consectetur adipiscing elit, sed do eiusmod tempor incididunt ut labore et dolore magna aliqua.</p>
  <div class="abs meta" style="left:22px;top:290px;color:#d0d0e6">
    <svg width="10" height="12" viewBox="0 0 10 12"><path d="M5 11.5S1 7 1 4.5a4 4 0 0 1 8 0C9 7 5 11.5 5 11.5z" fill="none" stroke="var(--gold)" stroke-width="1.3"/></svg>OAKLAND, CA</div>
  <div class="abs meta" style="left:22px;top:310px;color:#d0d0e6">
    <svg width="11" height="11" viewBox="0 0 11 11"><circle cx="5.5" cy="5.5" r="4.5" fill="none" stroke="#fff" stroke-width="1.2"/><path d="M5.5 3v2.7l1.8 1" fill="none" stroke="#fff" stroke-width="1.2"/></svg>7:00 p.m. PST</div>
  <div class="abs" style="left:22px;top:348px;padding:9px 18px;border:1.5px solid #d8d8ee;border-radius:5px;font-size:10.5px;color:#fff">Register Now</div>
</article>

<h3 class="abs upcoming-head">UPCOMING EVENTS</h3>
<div class="event-row" style="top:1896px;height:160px">
  <div class="date"><b>16</b><i></i><span>FEBRUARY</span></div>
  <div class="event-body">
    <h4>Infinite Possibilities Retreat</h4>
    <p>Lorem ipsum dolor sit amet, consectetur adipiscing elit, sed do eiusmod tempor incididunt ut labore et dolore magna aliqua.</p>
    <div class="meta"><svg width="10" height="12" viewBox="0 0 10 12"><path d="M5 11.5S1 7 1 4.5a4 4 0 0 1 8 0C9 7 5 11.5 5 11.5z" fill="none" stroke="var(--gold)" stroke-width="1.3"/></svg>SAN JOSÉ DEL CABO, MEXICO</div>
    <div class="meta"><svg width="11" height="11" viewBox="0 0 11 11"><circle cx="5.5" cy="5.5" r="4.5" fill="none" stroke="var(--navy)" stroke-width="1.2"/><path d="M5.5 3v2.7l1.8 1" fill="none" stroke="var(--navy)" stroke-width="1.2"/></svg>7:00 p.m. PST</div>
    <span class="link">Register Now</span> <span style="color:var(--navy)">⟶</span>
  </div>
</div>
<div class="abs" style="left:610px;top:2072px;width:410px;height:1px;background:#dcdce6"></div>
<div class="event-row" style="top:2093px;height:160px">
  <div class="date"><b>24</b><i></i><span>FEBRUARY</span></div>
  <div class="event-body">
    <h4>Infinite Possibilities Retreat</h4>
    <p>Lorem ipsum dolor sit amet, consectetur adipiscing elit, sed do eiusmod tempor incididunt ut labore et dolore magna aliqua.</p>
    <div class="meta"><svg width="10" height="12" viewBox="0 0 10 12"><path d="M5 11.5S1 7 1 4.5a4 4 0 0 1 8 0C9 7 5 11.5 5 11.5z" fill="none" stroke="var(--gold)" stroke-width="1.3"/></svg>SAN JOSÉ DEL CABO, MEXICO</div>
    <div class="meta"><svg width="11" height="11" viewBox="0 0 11 11"><circle cx="5.5" cy="5.5" r="4.5" fill="none" stroke="var(--navy)" stroke-width="1.2"/><path d="M5.5 3v2.7l1.8 1" fill="none" stroke="var(--navy)" stroke-width="1.2"/></svg>7:00 p.m. PST</div>
    <span class="link">Register Now</span> <span style="color:var(--navy)">⟶</span>
  </div>
</div>

<!-- About -->
<section class="abs about" aria-label="About us"></section>
<span class="sprig" style="left:312px;top:2410px" role="img" aria-label="Gold leaf accent"></span>
<h2 class="abs" style="left:252px;top:2452px;font-size:35px;font-weight:500;color:var(--ink)">About Us</h2>
<p class="abs" style="left:549px;top:2445px;width:400px;font-size:10.5px;line-height:1.45">Keffiyeh yr man braid, praxis poutine edison bulb enamel pin tone lyft. Chicharrones hell of master cleanse man braid organic chia. Kogi quinoa keytar mustache fixie kinfolk fingerstache. Bitters yes plz poke scenester.</p>

<div class="frame" style="left:252px;top:2537px;width:336px;height:367px;box-shadow:0 2px 12px rgba(60,60,90,.08)">
  <div class="photo" role="img" aria-label="Portrait of a smiling woman with wavy blonde hair" style="left:22px;top:22px;right:22px;bottom:22px;background:linear-gradient(160deg,#b7c08a,#7c8a4f 40%,#3a3d2c)"></div>
</div>
<div class="abs person" style="left:681px;top:2566px;width:300px">
  <h3>WILLA MARSH</h3>
  <p>Knausgaard single-origin coffee cronut, ascot plaid affogato kickstarter authentic tumeric la croix raw denim DSA banjo kombucha austin. Mkshk woke mukbang, marfa same retra asymmetrical.</p>
  <p>Affogato palo santo flexitarian hoodie, Gatekeep post-ironic air plant fixie tumeric pork belly.</p>
  <p class="spec">Specialties: Hatha Yoga, Kundalini Yoga, Sound Healing, Sound Bath with Crystal Singing Bowls</p>
</div>

<div class="abs person" style="left:252px;top:2998px;width:275px">
  <h3>JUNO REYES</h3>
  <p>Raw denim tote bag shabby chic air plant taiyaki DSA direct trade. Big mood activated charcoal ugh hot chicken disrupt Brooklyn hella plaid polaroid shaman bicycle rights art party raw denim. Forage tattooed knausgaard jianbing.</p>
  <p>Marfa pok pok chillwave, praxis snackwave bodega boys narwhal fanny pack echo park lomo blue bottle. Vape VHS deep v tbh sus activated charcoal PBR&amp;B craft beer palo santo beard paleo migas shabby chic fixie.</p>
  <p class="spec">Specialties: Reiki Energy Healing, Meditation, Breathwork, Massage, Reflexology</p>
</div>
<div class="frame" style="left:613px;top:2958px;width:332px;height:485px;box-shadow:0 2px 12px rgba(60,60,90,.08)">
  <div class="photo" role="img" aria-label="Portrait of a woman with long brown hair in a striped shirt at sunset" style="left:23px;top:23px;right:23px;bottom:23px;background:linear-gradient(170deg,#c98a4e,#7a5238 45%,#2f2a2c)"></div>
</div>

<!-- What We Do -->
<span class="sprig" style="left:578px;top:3585px" role="img" aria-label="Gold leaf accent"></span>
<h2 class="section-title" style="top:3624px">What We Do</h2>

<article class="service" style="left:180px;background:var(--navy)">
  <h3>Sound Healing</h3>
  <p>Godard letterpress subway tile bespoke. Raclette truffaut pork belly, yes plz succulents palo santo messenger bag sus cred. Keffiyeh austin PBR&amp;B subway tile put a bird on it cloud bread cliche.</p>
  <span class="btn" style="background:var(--violet)">Explore Now</span>
</article>
<article class="service" style="left:611px;background:var(--violet)">
  <h3>Meditation</h3>
  <p>Offal unicorn tumblr meditation waistcoat. Dreamcatcher cray shoreditch echo park. Migas kinfolk hexagon, banh mi blog ascot fanny pack gatekeep woke chambray sriracha.</p>
  <span class="btn" style="background:var(--navy)">Explore Now</span>
</article>

<!-- Wisdom -->
<section class="abs wisdom" aria-label="Wisdom posts"></section>
<span class="sprig" style="left:280px;top:4168px" role="img" aria-label="Gold leaf accent"></span>
<h2 class="abs" style="left:180px;top:4204px;font-size:35px;font-weight:500;color:var(--ink)">Wisdom Posts</h2>
<p class="abs" style="left:180px;top:4260px;width:440px;font-size:11.5px;line-height:1.55">I’m baby +1 farm-to-table taxidermy health goth unicorn, leggings selvage yuccie plaid coloring book woke hella gochujang.</p>
<span class="abs" style="left:879px;top:4256px;width:139px;height:38px;line-height:38px;text-align:center;background:var(--navy);color:#fff;font-size:11px;font-weight:600;border-radius:4px">See All Posts</span>

<article class="post" style="left:184px">
  <div class="thumb" role="img" aria-label="Silhouette in a tree yoga pose at sunset" style="background:linear-gradient(180deg,#e99b6d,#c45a4a 60%,#5a2f35)"></div>
  <h5>What Does Being Spiritual Look Like?</h5><small>by Tessa Lind | May 8, 2022</small><a>Read More</a>
</article>
<article class="post" style="left:399px">
  <div class="thumb" role="img" aria-label="Hands holding a singing bowl" style="background:linear-gradient(160deg,#e5e2dc,#c9b6a4 50%,#9b7256)"></div>
  <h5>Nine Ways to Help Others Awaken to Consciousness</h5><small>by Noel Brandt | May 8, 2022</small><a>Read More</a>
</article>
<article class="post" style="left:614px">
  <div class="thumb" role="img" aria-label="Person stretching on a mat viewed from above" style="background:linear-gradient(120deg,#3aa7a0,#4fb8b0 50%,#c89a72)"></div>
  <h5>Awakening Your Feminine Chakras</h5><small>by Ines Moreau | May 8, 2022</small><a>Read More</a>
</article>
<article class="post" style="left:829px">
  <div class="thumb" role="img" aria-label="Ancient temples at golden sunrise" style="background:linear-gradient(180deg,#f0c472,#d28d3b 60%,#5c3a1e)"></div>
  <h5>Treasures From The Distant Past</h5><small>by Hale Corwin | May 8, 2014</small><a>Read More</a>
</article>

<!-- Footer -->
<footer class="abs footer">
  <div class="abs" style="left:102px;top:56px;display:flex;align-items:center;gap:8px;font-weight:700;font-size:13px;letter-spacing:1.5px;color:var(--gold)"><span style="width:22px;height:22px;border-radius:50%;background:var(--lilac)"></span>luma grove</div>
  <p class="abs" style="left:102px;top:102px;width:260px;font-size:10px;line-height:1.6">Lorem ipsum dolor sit amet, consectetur adipiscing elit, sed do eiusmod tempor</p>
  <div class="abs" style="left:102px;top:146px;width:60px;height:1px;background:var(--gold)"></div>
  <p class="abs" style="left:102px;top:154px;font-size:9.5px">© 2022 Luma Grove. All Rights Reserved.</p>
  <div class="abs" style="left:461px;top:50px"><h6>Quick Links</h6><ul><li>Events</li><li>About Us</li><li>Synergise</li><li>Wisdom</li><li>Shop</li></ul></div>
  <div class="abs" style="left:605px;top:50px"><h6>Company</h6><ul><li>Terms of Use</li><li>Privacy Policy</li><li>Account</li><li>Cart</li><li>Orders</li></ul></div>
  <div class="abs" style="left:746px;top:52px"><h6>Follow Us</h6><div class="social"><span></span><span></span><span></span><span></span></div></div>
</footer>

</body>
</html>
```